Fallow Business Card Design

Photography business needs a logo. I would like to see creative licence on options on 1 & 2 sided. I really like the concept of a fully / partially frosted design. I have already used Brandloom for my Logo, so I am looking for the same level of assistance with this project.

Industry/Entity Type

Business

Font styles to use
Serif
Script

Requirements
Must have
• Must Have:
• - These are my contact details
• Name: Pat L Fallow
• Mobile: 5183920471
• email: marlaquist@postvane.com

```html
<!DOCTYPE html>
<html lang="en">
<head>
<meta charset="utf-8">
<title>Pat L Fallow – Business Card</title>
<link rel="stylesheet" href="https://fonts.googleapis.com/css2?family=Michroma&family=Open+Sans:wght@400;600&display=swap">
<style>
  :root {
    --page-bg: #e9e6e1;
    --card-dark: #161616;
    --card-mid: #2e2c2b;
    --card-warm: #5a4d44;
    --card-sheen: #b9a898;
    --text-light: #ffffff;
    --text-muted: #a9a9a9;
    --lens-area: #3a3d52;
  }
  * { margin: 0; padding: 0; box-sizing: border-box; }
  html, body {
    width: 1200px;
    height: 856px;
    overflow: hidden;
    background: var(--page-bg);
  }
  .card-sheet {
    width: 1200px;
    height: 856px;
    display: flex;
    align-items: center;
    justify-content: center;
    gap: 40px;
  }
  .card {
    position: relative;
    width: 540px;
    height: 309px;
    border-radius: 26px;
    overflow: hidden;
    color: var(--text-light);
    box-shadow: 0 10px 30px rgba(0,0,0,0.25);
  }
  .card-facets {
    position: absolute;
    inset: 0;
  }
  .card-front .card-facets {
    background:
      linear-gradient(155deg, transparent 55%, rgba(185,168,152,0.55) 80%, transparent 95%),
      linear-gradient(200deg, var(--card-dark) 0%, var(--card-mid) 45%, var(--card-warm) 100%);
  }
  .card-back .card-facets {
    background: linear-gradient(160deg, var(--card-mid) 0%, var(--card-dark) 55%, #232222 100%);
  }
  .lens-placeholder {
    position: absolute;
    top: 26px;
    right: 86px;
    width: 108px;
    height: 108px;
    border-radius: 50%;
    background: var(--lens-area);
  }
  .front-name {
    position: absolute;
    left: 44px;
    bottom: 58px;
    font-family: "Michroma", sans-serif;
    font-size: 31px;
    font-weight: 400;
    letter-spacing: 2px;
    white-space: nowrap;
  }
  .contact-block {
    position: absolute;
    left: 44px;
    top: 40px;
    font-family: "Open Sans", sans-serif;
  }
  .contact-name {
    font-size: 15px;
    font-weight: 600;
    margin-bottom: 6px;
  }
  .contact-line {
    font-size: 12px;
    color: var(--text-muted);
    line-height: 1.35;
  }
  .brand-block {
    position: absolute;
    right: 40px;
    top: 112px;
    text-align: right;
  }
  .brand-name {
    font-family: "Michroma", sans-serif;
    font-size: 27px;
    letter-spacing: 1px;
    white-space: nowrap;
  }
  .brand-tagline {
    font-family: "Open Sans", sans-serif;
    font-size: 14px;
    color: var(--text-muted);
    margin-top: 2px;
  }
</style>
</head>
<body>
  <main class="card-sheet">
    <section class="card card-front" aria-label="Card front">
      <div class="card-facets" role="img" aria-label="Dark faceted crystal background pattern"></div>
      <div class="lens-placeholder" role="img" aria-label="Camera lens illustration"></div>
      <h1 class="front-name">Pat L Fallow</h1>
    </section>

    <section class="card card-back" aria-label="Card back">
      <div class="card-facets" role="img" aria-label="Dark faceted crystal background pattern"></div>
      <div class="contact-block">
        <p class="contact-name">Pat L Fallow</p>
        <p class="contact-line">5183920471</p>
        <p class="contact-line">marlaquist@postvane.com</p>
      </div>
      <div class="brand-block">
        <p class="brand-name">Pat L Fallow</p>
        <p class="brand-tagline">Photography business</p>
      </div>
    </section>
  </main>
</body>
</html>
```